Media/PR business needs a website upgrade

Modernise my website www.pvl.net.au into a simpler and mobile friendly site with the usual plugins, maximum 5 pages, 4 might be enough. My page is already hosted and I have an email address so I just want to work with a designer who is fantastic with WordPress, to refresh and simplify the 6 year-old look.

Target Market(s)

men & women 25-55

Industry/Entity Type

Business

Coding

Coded - Design and coding required

Number of Pages Required

4 page

Font styles to use
Sans Serif

Colors
f37122
ffffff

Requirements
Must have
• Social media plugins, about, client portfolio, contact (can be under about)blog capability
Nice to have
• photos of jobs I've done
Should not have
• e-commerce, can lose all the client logos

```html
<!DOCTYPE html>
<html lang="en">
<head>
<meta charset="utf-8">
<title>Pivot Line Communications</title>
<link href="https://fonts.googleapis.com/css2?family=Roboto:wght@300;400;500;700&family=Open+Sans:ital,wght@0,300;0,400;0,600;1,300;1,400&display=swap" rel="stylesheet">
<style>
:root{
  --orange:#f37122;
  --orange-warm:#ffa000;
  --red-warm:#d6473f;
  --white:#ffffff;
  --ink:#333333;
  --black:#000000;
  --rule:#8a8a8a;
  --caption-blue:#1f5fa8;
  --hero-light:#f2f3f6;
  --hero-mid:#e4e5ea;
  --hero-warm:#e6ddd6;
}
*{margin:0;padding:0;box-sizing:border-box}
html,body{width:974px;height:1200px;overflow:hidden;background:var(--white)}
body{position:relative;font-family:'Open Sans',sans-serif;color:var(--ink)}
.abs{position:absolute}

/* hero */
.hero{left:0;top:0;width:974px;height:322px;overflow:hidden}
.hero-photo{position:absolute;inset:0;background:linear-gradient(100deg,var(--hero-light) 0%,var(--hero-mid) 60%,var(--hero-warm) 100%)}
.brand{left:58px;top:34px;display:flex;align-items:center;gap:8px}
.brand-dot{width:75px;height:75px;border-radius:50%;background:var(--orange)}
.brand-name{font-family:'Roboto',sans-serif;font-weight:500;font-size:17px;line-height:17px;color:var(--ink)}
.main-nav{left:339px;top:62px;display:flex;font-family:'Roboto',sans-serif;font-weight:300;font-size:16px;color:#3a3a3a}
.main-nav a{color:inherit;text-decoration:none;margin-right:31px}
.main-nav a.active{color:var(--orange)}
.main-nav a:nth-child(3){margin-right:35px}
.hero-title{left:58px;top:145px;width:420px;font-family:'Roboto',sans-serif;font-weight:700;font-size:25px;line-height:32px;color:#333}
.hero-call{left:648px;top:242px;width:326px;height:38px;background:var(--orange);clip-path:polygon(12px 0,100% 0,100% 100%,0 100%)}
.hero-call span{position:absolute;left:13px;top:2px;font-family:'Roboto',sans-serif;font-weight:700;font-size:25px;color:var(--white)}

/* about */
.about{left:0;top:322px;width:603px;height:366px;text-align:center}
.section-title{font-family:'Roboto',sans-serif;font-weight:700;font-size:34px;color:#111;margin-top:23px}
.title-rule{width:116px;height:3px;background:var(--orange);margin:7px auto 0}
.about-text{width:410px;margin:14px auto 0;font-size:17px;line-height:21.6px;color:#222}

/* expertise */
.expertise{left:0;top:688px;width:398px;height:303px;background:var(--orange);color:var(--white)}
.expertise h2{position:absolute;left:66px;top:10px;font-family:'Roboto',sans-serif;font-weight:700;font-size:31px}
.expertise .rule{position:absolute;left:171px;top:60px;width:114px;height:3px;background:var(--white)}
.skill{position:absolute;font-weight:600;font-size:17px;white-space:nowrap}
.portrait{left:398px;top:688px;width:205px;height:303px;background:linear-gradient(180deg,#e9e6df 0%,#d6d1c8 100%)}
.portrait-caption{position:absolute;right:8px;top:6px;font-style:italic;font-size:11px;color:var(--caption-blue)}

/* posts */
.posts{left:603px;top:322px;width:371px;height:669px;background:linear-gradient(150deg,var(--orange-warm) 0%,var(--orange) 45%,var(--red-warm) 100%)}
.posts-label{position:absolute;left:0;top:19px;width:222px;height:45px;background:var(--black);color:var(--white);font-family:'Roboto',sans-serif;font-weight:500;font-size:25px;line-height:45px;padding-left:37px}
.timeline{position:absolute;left:25px;top:121px;width:5px;height:515px;background:var(--white)}
.post-dot{position:absolute;left:19px;width:17px;height:17px;border-radius:50%;background:var(--orange);border:3px solid var(--white)}
.post{position:absolute;left:51px;width:240px;color:var(--white)}
.post h3{font-weight:300;font-size:25px;line-height:31px}
.post time{display:block;margin-top:5px;font-style:italic;font-weight:300;font-size:16px}

/* footer */
.footer{left:0;top:991px;width:974px;height:209px;background:var(--black);color:var(--white);font-family:'Roboto',sans-serif}
.foot-nav{position:absolute;left:67px;top:26px;display:flex;font-weight:700;font-size:17px}
.foot-nav a{color:inherit;text-decoration:none;padding:0 21px;border-left:1px solid #aaa;line-height:18px}
.foot-nav a:first-child{padding-left:0;border-left:none}
.social{position:absolute;right:57px;top:26px;display:flex;gap:28px;font-weight:500;font-size:17px}
.foot-rule{position:absolute;left:58px;top:71px;width:859px;height:1px;background:var(--rule)}
.contact-row{position:absolute;top:106px;display:flex;align-items:center;gap:9px;font-weight:300;font-size:17px}
.abn{position:absolute;left:0;top:146px;width:327px;height:39px;background:var(--orange);clip-path:polygon(0 0,312px 0,100% 100%,0 100%)}
.abn span{position:absolute;left:60px;top:3px;font-weight:500;font-size:26px}
.copyright{position:absolute;right:57px;top:157px;font-weight:300;font-size:16px}
</style>
</head>
<body>

<header class="abs hero">
  <div class="hero-photo" role="img" aria-label="Header photograph area"></div>
  <div class="abs brand">
    <span class="brand-dot"></span>
    <span class="brand-name">Pivot<br>Line<br>Communications</span>
  </div>
  <nav class="abs main-nav">
    <a class="active" href="#">Home</a><a href="#">Services</a><a href="#">About</a><a href="#">Portfolio</a><a href="#">Contact Us</a>
  </nav>
  <h1 class="abs hero-title">We are an established specialist public relations and event management business.</h1>
  <div class="abs hero-call"><span>Contact 0400 555 019</span></div>
</header>

<section class="abs about">
  <h2 class="section-title">About Us</h2>
  <div class="title-rule"></div>
  <div class="about-text">
    <p>With a communications degree and 20 plus years experience working in public relations, publicity, media and project management, PVL founder Dana Whitfield offers a complete contract based option for your next major sporting, social, cultural or community event.</p>
    <p>Contact Dana at PVL for strategic advice on sponsorship spend and how to leverage your investment, and to tap into her extensive media and professional network.</p>
    <p>Flexible, composed and relationship focused freelancer ready to start work.</p>
  </div>
</section>

<section class="abs expertise">
  <h2>Key areas of expertise</h2>
  <div class="rule"></div>
  <span class="skill" style="left:67px;top:77px">Sports media</span>
  <span class="skill" style="left:274px;top:77px">Publicity</span>
  <span class="skill" style="left:67px;top:113px">Sponsorship leverage</span>
  <span class="skill" style="left:274px;top:113px">Storytelling</span>
  <span class="skill" style="left:67px;top:149px">Event management</span>
  <span class="skill" style="left:274px;top:149px">Social media</span>
  <span class="skill" style="left:67px;top:184px">Crisis management</span>
  <span class="skill" style="left:67px;top:220px">Writing &amp; editing web, newsletter and</span>
  <span class="skill" style="left:67px;top:256px">magazine content</span>
</section>

<div class="abs portrait" role="img" aria-label="Portrait photo of the founder">
  <span class="portrait-caption">PVL - Dana Whitfield</span>
</div>

<aside class="abs posts">
  <div class="posts-label">Latest posts</div>
  <div class="timeline"></div>
  <span class="post-dot" style="top:113px"></span>
  <span class="post-dot" style="top:288px"></span>
  <span class="post-dot" style="top:461px"></span>
  <article class="post" style="top:106px">
    <h3>Opinion: Harbour Cup runneth over with blokes</h3>
    <time>May 31st, 2017 by Dana Whitfield</time>
  </article>
  <article class="post" style="top:281px">
    <h3>A normal day in Rio</h3>
    <time>May 31st, 2017 by Dana Whitfield</time>
  </article>
  <article class="post" style="top:454px">
    <h3>Opinion: Harbour Cup runneth over with blokes</h3>
    <time>May 31st, 2017 by Dana Whitfield</time>
  </article>
</aside>

<footer class="abs footer">
  <nav class="foot-nav">
    <a href="#">Home</a><a href="#">Services</a><a href="#">About</a><a href="#">Portfolio</a><a href="#">Contact Us</a>
  </nav>
  <div class="social"><span>CHIRPER</span><span>FRIENDBOOK</span><span>LINKPRO</span></div>
  <div class="foot-rule"></div>
  <div class="contact-row" style="left:76px">
    <svg width="14" height="19" viewBox="0 0 14 19"><path d="M7 0C3.1 0 0 3.1 0 7c0 5 7 12 7 12s7-7 7-12c0-3.9-3.1-7-7-7zm0 9.5A2.5 2.5 0 1 1 7 4.5a2.5 2.5 0 0 1 0 5z" fill="#f37122"/></svg>
    <span>PO Box 2240, Harbour Vale NSW 2199 Australia</span>
  </div>
  <div class="contact-row" style="left:466px">
    <svg width="20" height="20" viewBox="0 0 24 24"><path d="M6.6 10.8a15.2 15.2 0 0 0 6.6 6.6l2.2-2.2c.3-.3.7-.4 1-.2 1.1.4 2.3.6 3.6.6.6 0 1 .4 1 1V20c0 .6-.4 1-1 1C10.6 21 3 13.4 3 4c0-.6.4-1 1-1h3.5c.6 0 1 .4 1 1 0 1.3.2 2.5.6 3.6.1.3 0 .7-.2 1l-2.3 2.2z" fill="#f37122"/></svg>
    <span>+61 400 555 019</span>
  </div>
  <div class="contact-row" style="left:661px">
    <svg width="25" height="18" viewBox="0 0 25 18"><rect width="25" height="18" rx="2" fill="#f37122"/><path d="M1 2l11.5 8L24 2" stroke="#000" stroke-width="2" fill="none"/></svg>
    <span style="margin-left:8px">dana@pvl.net.au</span>
  </div>
  <div class="abn"><span>ABN: 12 345 678 901</span></div>
  <div class="copyright">© 2017 Pivot Line Communications</div>
</footer>

</body>
</html>
```